Financial Advisor needs waiting room sign

I am a financial advisor that works with a number of accountants to develop prospects. I am looking for a 18"x24" sign to hang in their office waiting rooms to help develop prospect interest in my services. My original idea was to list all of our services in a jumbled way on the sign and on the bottom have something like "Confused? We have the answers?" "Questions - We have answers" Our logo on the bottom. While I think this is still a good idea when I try to design it - it does not work. I am open to other ideas. Here is a list of our services (list in no particular order) and I will attach our logo. List: Plovance, Plovance Supplement, Plovance Advantage, Truvely, Part A, Part B, Part D, Social Security, Turning 65, Annuities, Fixed Index Annuities, Rollovers, 401k, 403b, Investments, Stock Market, Mutual Funds, Term Insurance, Life Insurance, Final Expense, Long Term Care, Mortgage Protection, 403B / 457 Not for Profit Set Up, 403B / TSA Plans, Annuities, Asset Protection, Charitable Giving, College Funding, Estate Planning, Fixed Indexed Annuities, Guaranteed Income, IRA & 401(K) Assets and Planning, IRA, 401(K), 403(B) Rollovers, Lifetime Income Planning, Retirement Income Planning, Safe Money Options, Social Security, Tactical Asset Allocation

```html
<!DOCTYPE html>
<html lang="en">
<head>
<meta charset="utf-8">
<title>Harlowe Capital – Waiting Room Sign</title>
<link rel="stylesheet" href="https://fonts.googleapis.com/css2?family=Roboto+Condensed:wght@400;700;900&display=swap">
<style>
  :root {
    --page: #f4f4f4;
    --ink-black: #1f1f20;
    --ink-dark: #2b2b2c;
    --ink-grey: #7b7c7e;
    --brand-green: #5a9a32;
    --panel-top: #eceeef;
    --panel-bottom: #d6d8da;
    --white: #ffffff;
  }
  html, body {
    margin: 0;
    width: 1200px;
    height: 1200px;
    overflow: hidden;
    background: var(--page);
  }
  .sign {
    position: absolute;
    left: 20px;
    top: 162px;
    width: 1160px;
    height: 876px;
    display: block;
    font-family: "Roboto Condensed", "Arial Narrow", sans-serif;
  }
  .headline { fill: var(--white); font-weight: 900; }
  .subhead { fill: var(--brand-green); font-weight: 700; }
  .business-name { fill: var(--ink-dark); font-weight: 700; }
  .term { font-weight: 700; }
  .term--grey { fill: var(--ink-grey); }
  .term--dark { fill: var(--ink-dark); }
  .term--light { font-weight: 400; }
</style>
</head>
<body>
<svg class="sign" viewBox="0 0 980 740" xmlns="http://www.w3.org/2000/svg" role="img" aria-label="Harlowe Capital waiting room sign listing insurance and financial services">
  <defs>
    <linearGradient id="panelFill" x1="0" y1="0" x2="0" y2="1">
      <stop offset="0" stop-color="var(--panel-top)"/>
      <stop offset="1" stop-color="var(--panel-bottom)"/>
    </linearGradient>
  </defs>

  <rect class="panel" width="980" height="740" fill="url(#panelFill)"/>

  <path class="header-swoosh-green" fill="var(--brand-green)"
        d="M0 168 C160 205 330 215 500 150 C620 105 720 70 800 58 L980 58 L980 66 C820 66 700 95 560 150 C380 222 180 225 0 184 Z"/>
  <path class="header-band" fill="var(--ink-black)"
        d="M0 0 H980 V58 C800 50 640 80 500 140 C330 205 160 198 0 168 Z"/>
  <path class="header-swoosh-accent" fill="var(--brand-green)"
        d="M590 128 C700 88 840 70 980 78 L980 112 C880 92 740 100 590 128 Z"/>

  <text class="headline" x="38" y="102" font-size="96" textLength="466" lengthAdjust="spacingAndGlyphs">CONFUSED?</text>
  <text class="subhead" x="38" y="143" font-size="30" textLength="322" lengthAdjust="spacingAndGlyphs">WE HAVE THE ANSWERS?</text>

  <!-- business name -->
  <rect class="business-mark" x="700" y="186" width="20" height="20" fill="var(--ink-dark)"/>
  <text class="business-name" x="730" y="205" font-size="28">Harlowe Capital</text>

  <g class="services">
    <text class="term term--grey" x="138" y="303" font-size="36" textLength="167" lengthAdjust="spacingAndGlyphs">MORTGAGE</text>
    <text class="term term--dark" x="310" y="302" font-size="36" textLength="150" lengthAdjust="spacingAndGlyphs">Annuities</text>
    <text class="term term--grey" x="468" y="303" font-size="38" textLength="302" lengthAdjust="spacingAndGlyphs">SOCIAL SECURITY</text>
    <text class="term term--grey" x="118" y="340" font-size="36" textLength="187" lengthAdjust="spacingAndGlyphs">PROTECTION</text>
    <text class="term term--grey" transform="translate(310 315) rotate(90)" font-size="36" textLength="270" lengthAdjust="spacingAndGlyphs">FINAL EXPENSE</text>
    <text class="term term--grey" x="352" y="360" font-size="72" textLength="298" lengthAdjust="spacingAndGlyphs">PLOVANCE</text>
    <text class="term term--grey" transform="translate(685 430) rotate(-90)" font-size="32" textLength="120" lengthAdjust="spacingAndGlyphs">Truvely</text>
    <text class="term term--dark" x="700" y="340" font-size="34" textLength="77" lengthAdjust="spacingAndGlyphs">401k</text>
    <text class="term term--dark" x="700" y="360" font-size="20" textLength="48" lengthAdjust="spacingAndGlyphs">403b</text>
    <text class="term term--grey" x="785" y="362" font-size="30" textLength="150" lengthAdjust="spacingAndGlyphs">Guaranteed</text>
    <text class="term term--dark term--light" x="115" y="370" font-size="28" textLength="190" lengthAdjust="spacingAndGlyphs">Charitable Giving</text>
    <text class="term term--dark term--light" x="352" y="390" font-size="19" textLength="94" lengthAdjust="spacingAndGlyphs">IRA, 401(K),</text>
    <text class="term term--dark" x="450" y="390" font-size="19" textLength="202" lengthAdjust="spacingAndGlyphs">Plovance Supplement</text>
    <text class="term term--dark term--light" x="698" y="396" font-size="32" textLength="137" lengthAdjust="spacingAndGlyphs">ANNUITIES</text>
    <text class="term term--grey" x="840" y="395" font-size="30" textLength="95" lengthAdjust="spacingAndGlyphs">Income</text>
    <text class="term term--grey" x="203" y="408" font-size="36" textLength="102" lengthAdjust="spacingAndGlyphs">403B /</text>
    <text class="term term--dark" transform="translate(80 375) rotate(90)" font-size="22" textLength="177" lengthAdjust="spacingAndGlyphs">LIFETIME INCOME</text>
    <text class="term term--dark" transform="translate(53 450) rotate(90)" font-size="22" textLength="102" lengthAdjust="spacingAndGlyphs">PLANNING</text>
    <text class="term term--grey" x="352" y="428" font-size="34" textLength="298" lengthAdjust="spacingAndGlyphs">Plovance Advantage</text>
    <text class="term term--grey" x="698" y="440" font-size="50" textLength="240" lengthAdjust="spacingAndGlyphs">ROLLOVERS</text>
    <text class="term term--grey" x="138" y="445" font-size="36" textLength="167" lengthAdjust="spacingAndGlyphs">TSA PLANS</text>
    <text class="term term--dark term--light" x="352" y="458" font-size="22" textLength="148" lengthAdjust="spacingAndGlyphs">STOCK MARKET</text>
    <text class="term term--grey" transform="translate(540 608) rotate(-90)" font-size="36" textLength="170" lengthAdjust="spacingAndGlyphs">Turning 65</text>
    <text class="term term--grey" x="548" y="470" font-size="34" textLength="145" lengthAdjust="spacingAndGlyphs">Part A,B,D</text>
    <text class="term term--dark" x="695" y="468" font-size="22" textLength="143" lengthAdjust="spacingAndGlyphs">INVESTMENTS</text>
    <text class="term term--grey" transform="translate(843 447) rotate(90)" font-size="24" textLength="196" lengthAdjust="spacingAndGlyphs">LONG TERM CARE</text>
    <text class="term term--grey term--light" transform="translate(878 447) rotate(90)" font-size="26" textLength="193" lengthAdjust="spacingAndGlyphs">Income Planning</text>
    <text class="term term--grey term--light" transform="translate(908 447) rotate(90)" font-size="26" textLength="130" lengthAdjust="spacingAndGlyphs">Retirement</text>
    <text class="term term--dark" x="115" y="480" font-size="24" textLength="190" lengthAdjust="spacingAndGlyphs">403(B) Rollovers</text>
    <text class="term term--dark" x="352" y="487" font-size="24" textLength="148" lengthAdjust="spacingAndGlyphs">Mutual Funds</text>
    <text class="term term--grey" x="112" y="520" font-size="34" textLength="106" lengthAdjust="spacingAndGlyphs">ESTATE</text>
    <text class="term term--grey" transform="translate(225 488) rotate(90)" font-size="40" textLength="157" lengthAdjust="spacingAndGlyphs">FUNDING</text>
    <text class="term term--grey" transform="translate(265 488) rotate(90)" font-size="40" textLength="157" lengthAdjust="spacingAndGlyphs">COLLEGE</text>
    <text class="term term--dark" x="352" y="513" font-size="22" textLength="146" lengthAdjust="spacingAndGlyphs">Life Insurance</text>
    <text class="term term--dark term--light" x="548" y="507" font-size="34" textLength="289" lengthAdjust="spacingAndGlyphs">Fixed Index Annuities</text>
    <text class="term term--grey" x="112" y="545" font-size="24" textLength="106" lengthAdjust="spacingAndGlyphs">PLANNING</text>
    <text class="term term--dark" x="548" y="534" font-size="20" textLength="289" lengthAdjust="spacingAndGlyphs">TERM INSURANCE, IRA, 401(K)</text>
    <text class="term term--grey" x="352" y="558" font-size="34" textLength="148" lengthAdjust="spacingAndGlyphs">FIXED INDEXED</text>
    <text class="term term--dark term--light" x="548" y="562" font-size="20" textLength="287" lengthAdjust="spacingAndGlyphs">IRA &amp; 401(K) Assets and Planning</text>
    <text class="term term--grey" x="86" y="595" font-size="40" textLength="132" lengthAdjust="spacingAndGlyphs">SOCIAL</text>
    <text class="term term--grey" x="352" y="600" font-size="34" textLength="105" lengthAdjust="spacingAndGlyphs">ANNUITIES</text>
    <text class="term term--grey" x="548" y="602" font-size="34" textLength="282" lengthAdjust="spacingAndGlyphs">ASSET PROTECTION</text>
    <text class="term term--grey" x="40" y="638" font-size="40" textLength="178" lengthAdjust="spacingAndGlyphs">SECURITY</text>
    <text class="term term--dark term--light" x="310" y="643" font-size="40" textLength="520" lengthAdjust="spacingAndGlyphs">403B / 457 Not for Profit Set Up</text>
    <text class="term term--dark term--light" x="140" y="686" font-size="34" textLength="333" lengthAdjust="spacingAndGlyphs">Tactical Asset Allocation</text>
    <text class="term term--grey" x="480" y="688" font-size="48" textLength="455" lengthAdjust="spacingAndGlyphs">SAFE MONEY OPTIONS</text>
  </g>
</svg>
</body>
</html>
```